Broschüre Notduschen Topseller
Zielgruppe
Ein familiengeführtes und mittelständisches Unternehmen mit unterschiedlichen Geschäftsbereichen.
K-VORTAL* ist bereits seit Mitte der 80er Jahre als Anbieter von Augenduschen und Notduschen in Deutschland bekannt und hat den Marktanteil durch die konsequente Erweiterung der Produktpalette in Verbindung mit dem höchstmöglichen Qualitätsanspruch kontinuierlich ausgebaut. Bereits im Jahre 2008 wurde die Marke K-VORTAL für professionelle Notduschsysteme und Arbeitsschutzprodukte am Markt etabliert. Seit dem 01.01.2012 firmiert K-VORTAL auch als K-VORTAL GmbH und ist heute einer der führenden Hersteller für Notduschen und Augenduschen in Europa.
Aufgabenstellung
In der word Datei ist soweit alles selbsterklärend. Zwischen den Texten ist vermerkt,
was an Bildern und Logos dazu kommt. Fehlende Daten (Logo und weitere Bilder) senden
wir dann noch, mehr konnten wir hier nicht einstellen.
Mischung aus technischer Beschreibung und Katalog
Broschüre, beidseitig bedruckt, DIN A4 Format
Wenn chic, dann zukünftig auch mehr Broschüren.

```html
<!DOCTYPE html>
<html lang="de">
<head>
<meta charset="utf-8">
<title>Augenduschen BasisLine – Hand-Augenduschen</title>
<link href="https://fonts.googleapis.com/css2?family=Ubuntu:wght@400;500;700&family=Roboto:wght@400;500&display=swap" rel="stylesheet">
<style>
  :root{
    --bg:#e3e3e4;
    --page:#fbfbfb;
    --panel:#ececee;
    --card:#f7f7f8;
    --green:#5b9e1f;
    --green-light:#9fd062;
    --purple:#4c1f6e;
    --purple-head:#4a1b70;
    --ink:#2a2a2a;
    --rule:#6d6d6d;
    --url:#5aa31d;
  }
  *{margin:0;padding:0;box-sizing:border-box}
  html,body{width:1200px;height:1200px;overflow:hidden;background:var(--bg)}
  body{font-family:'Roboto',sans-serif;color:var(--ink);position:relative}
  .spread{position:absolute;left:20px;top:180px;width:1160px;height:841px}
  .page{position:absolute;top:0;width:580px;height:841px;background:var(--page)}
  .page--left{left:0}
  .page--right{left:580px}
  .abs{position:absolute}

  .band-title{background:var(--green);color:#fff;font-family:'Ubuntu',sans-serif;font-weight:700;font-size:23px;display:flex;align-items:center;padding:0 16px}
  .band-sub{background:var(--purple);color:#fff;font-family:'Ubuntu',sans-serif;font-size:15px;display:flex;align-items:center;padding:0 16px}
  .band--right{justify-content:flex-end}

  .panel{background:var(--panel)}

  .section-title{font-family:'Ubuntu',sans-serif;font-weight:700;font-size:23px;color:var(--purple-head)}
  .intro{font-size:11px;line-height:15px;width:240px}

  .photo{background:linear-gradient(135deg,#c9d9d3 0%,#e6ebe8 40%,#b9a08a 60%,#d8e2df 100%)}

  .feature-card{background:var(--card)}
  .bar{height:27px;background:linear-gradient(90deg,var(--green) 0%,var(--green) 50%,var(--green-light) 100%);color:#fff;font-family:'Ubuntu',sans-serif;font-weight:500;font-size:14px;display:flex;align-items:center;padding-left:14px}
  .bullets{list-style:none;font-size:11px;line-height:15px}
  .bullets li{position:relative;padding-left:21px;margin-bottom:5px}
  .bullets li::before{content:"";position:absolute;left:12px;top:6px;width:4px;height:4px;border-radius:50%;background:var(--green)}
  .bullets--tight li{margin-bottom:6px}

  .product{background:var(--card);width:164px;height:588px;top:195px}
  .product-image{position:absolute;left:0;top:0;width:164px;height:262px;background:linear-gradient(180deg,#f2f2f3,#e9ecea)}
  .product-code{position:absolute;left:0;top:262px;width:164px;height:28px;background:var(--green);color:#fff;font-family:'Ubuntu',sans-serif;font-weight:500;font-size:16px;display:flex;align-items:center;padding-left:12px}
  .product-desc{position:absolute;left:8px;top:308px;font-size:11px;line-height:15px}
  .spec{position:absolute;left:0;width:164px;border-top:1px solid var(--rule);padding:8px 8px 0;font-size:11px;line-height:15px}

  .folio{font-size:10px;font-weight:500;top:819px}
  .url{font-size:11px;color:var(--url);font-weight:500;top:817px}
</style>
</head>
<body>
<div class="spread">
  <section class="page page--left">
    <div class="abs band-title" style="left:0;top:30px;width:243px;height:46px">Augenduschen</div>
    <div class="abs band-sub" style="left:0;top:76px;width:243px;height:33px">BasisLine</div>

    <div class="abs panel" style="left:14px;top:134px;width:552px;height:662px"></div>

    <h1 class="abs section-title" style="left:32px;top:191px">Hand-Augenduschen</h1>
    <p class="abs intro" style="left:32px;top:226px">Zwei Duschen in einer - das ist möglich durch die einzigartige Konstruktion dieser Duschen: die Hand-Augenduschen können als fest installierte Augendusche in der Halterung betrieben werden; oder aber aus der Halterung entnommen werden, um als Handbrause am Boden liegende Verletzte zu versorgen.<br>Wählen Sie aus einer Vielzahl von Modellen mit einem oder zwei Brauseköpfen.</p>

    <div class="abs photo" role="img" aria-label="Foto: Person spült sich die Augen an einer wandmontierten Hand-Augendusche" style="left:30px;top:435px;width:244px;height:348px"></div>

    <div class="abs feature-card" style="left:291px;top:195px;width:247px;height:588px">
      <div class="bar">Produktmerkmale</div>
      <ul class="bullets" style="margin-top:15px;padding-right:10px">
        <li>K-VORTAL Hochleistungsbrauseköpfe für einen begrenzten, gleichmäßigen und weichen Wasserstrahl – optimiert für das Ausspülen von Chemikalien im Auge.</li>
        <li>Integrierter automatischer Mengenregulator für die richtige Strahlhöhe unabhängig vom Wasserdruck.</li>
        <li>Integrierter Rückflussverhinderer zum Schutz des Trinkwassernetzes.</li>
        <li>Gummimuffen um den Brausekopf schützen den Hilfesuchenden vor Stoßverletzungen.</li>
        <li>Staubabdeckkappen öffnen bei Betätigung der Augendusche durch den Wasserdruck selbständig.</li>
        <li>Große Bohrungen in den Brauseköpfen verhindern stehendes Wasser und somit Verkalkung.</li>
      </ul>
      <div class="bar abs" style="left:0;top:344px;width:247px">Technische Daten:</div>
      <ul class="bullets bullets--tight abs" style="left:0;top:382px">
        <li>Wasseranschluss: 1/2-Zoll-IG</li>
        <li>Schlauchlänge: 1500 mm</li>
        <li>Volumenstrom: 7 l/min pro Brausekopf</li>
      </ul>
      <div class="bar abs" style="left:0;top:461px;width:247px">Normen / Zulassungen:</div>
      <ul class="bullets bullets--tight abs" style="left:0;top:499px">
        <li>DIN EN 15154-2:2006, ANSI Z358.1-2014</li>
        <li>ZPWV, NW-0583KV0419</li>
      </ul>
    </div>

    <div class="abs folio" style="left:25px">4</div>
    <div class="abs url" style="right:40px">www.k-vortal.com</div>
  </section>

  <section class="page page--right">
    <div class="abs band-title band--right" style="right:2px;top:32px;width:253px;height:47px">Augenduschen</div>
    <div class="abs band-sub band--right" style="right:2px;top:79px;width:253px;height:33px">BasisLine</div>

    <div class="abs panel" style="left:0;top:136px;width:562px;height:661px"></div>

    <article class="abs product" style="left:21px">
      <div class="product-image" role="img" aria-label="Produktfoto: Hand-Augendusche mit einem Brausekopf in Halterung"></div>
      <div class="product-code">KV 512 040</div>
      <p class="product-desc">BasisLine<br>Hand-Augendusche<br>mit einem Brausekopf,<br>für Wand-/Tischmontage.</p>
      <div class="spec" style="top:390px">Abmessungen: (L x B x H)<br>380 x 290 x 100 mm</div>
      <div class="spec" style="top:439px">Gewicht:<br>1,30 kg</div>
      <div class="spec" style="top:489px">PG<br>86</div>
      <div class="spec" style="top:539px">Preis / Stück<br>195,00 €</div>
    </article>

    <article class="abs product" style="left:201px">
      <div class="product-image" role="img" aria-label="Produktfoto: Hand-Augendusche mit einem Brausekopf 45° in Halterung"></div>
      <div class="product-code">KV 513 040</div>
      <p class="product-desc">BasisLine<br>Hand-Augendusche<br>mit einem Brausekopf 45°,<br>für Wand-/Tischmontage.</p>
      <div class="spec" style="top:390px">Abmessungen: (L x B x H)<br>380 x 290 x 100 mm</div>
      <div class="spec" style="top:439px">Gewicht:<br>1,34 kg</div>
      <div class="spec" style="top:489px">PG<br>86</div>
      <div class="spec" style="top:539px">Preis / Stück<br>235,00 €</div>
    </article>

    <article class="abs product" style="left:381px">
      <div class="product-image" role="img" aria-label="Produktfoto: Hand-Augendusche mit zwei Brauseköpfen 45° in Halterung"></div>
      <div class="product-code">KV 514 040</div>
      <p class="product-desc">BasisLine<br>Hand-Augendusche<br>mit zwei Brauseköpfen 45°,<br>für Wand-/Tischmontage.</p>
      <div class="spec" style="top:390px">Abmessungen: (L x B x H)<br>380 x 290 x 100 mm</div>
      <div class="spec" style="top:439px">Gewicht:<br>1,44 kg</div>
      <div class="spec" style="top:489px">PG<br>86</div>
      <div class="spec" style="top:539px">Preis / Stück<br>260,00 €</div>
    </article>

    <div class="abs url" style="left:22px">www.k-vortal.com</div>
    <div class="abs folio" style="right:30px">5</div>
  </section>
</div>
</body>
</html>
```